Velmora Steam Cleaning website for demos

Velmora Steam Cleaning is a business that provides commercial cleaning services utilizing steam vapor, which offers the most effective and ecologically friendly method of cleaning today. We need a website to advertise our services, and needs to incorporate spaces to show video demonstrations on how the cleaning machine works.

Target Market(s)

The potential market for this business are hotels, motels, restaurants, hospitals, fast food facilities, nursing homes, day care centers, schools, country clubs, churches, office and apartment buildings, malls, movie theaters, super markets, airports, parks, and any other facility.

Industry/Entity Type

Business

Coding

Coded - Design and coding required

Number of Pages Required

3 page

Colors
add136
9bcb3c
34a6d7
3176b5
edf8f6

Requirements
Must have
• Areas for videos that serve as demonstrations of our services

```html
<!DOCTYPE html>
<html lang="en">
<head>
<meta charset="utf-8">
<title>Velmora Steam Cleaning</title>
<link rel="stylesheet" href="https://fonts.googleapis.com/css2?family=Lato:wght@400;700;900&family=Michroma&display=swap">
<style>
:root{
  --blue:#0b73dc;
  --blue-dark:#075fb8;
  --green:#5c9f39;
  --green-light:#7cbf3e;
  --teal-dark:#0b3444;
  --teal:#15536a;
  --ink:#222;
  --grey-text:#555;
  --panel:#f2f2f2;
  --white:#fff;
}
*{margin:0;padding:0;box-sizing:border-box}
html,body{width:772px;height:1200px;overflow:hidden;background:var(--white)}
body{position:relative;font-family:"Lato",sans-serif;color:var(--ink)}
.abs{position:absolute}
.display{font-family:"Michroma",sans-serif;font-style:italic;text-transform:uppercase}

/* header */
.site-header{left:0;top:0;width:772px;height:72px;background:linear-gradient(#fff,#eef3f8)}
.brand{left:60px;top:18px;display:flex;align-items:center;gap:8px}
.brand-dot{width:34px;height:34px;border-radius:50%;background:var(--green-light)}
.brand-name{font-weight:900;font-size:17px;color:var(--blue);line-height:1}
.address{right:62px;top:14px;font-size:8.5px;color:#444;display:flex;align-items:center;gap:5px}
.main-nav{left:283px;top:39px;width:489px;height:31px;background:var(--blue);clip-path:polygon(10px 0,100% 0,100% 100%,0 100%)}
.main-nav ul{list-style:none;display:flex;height:100%;padding-left:16px}
.main-nav li{height:100%;display:flex;align-items:center;justify-content:center;color:var(--white);font-size:8.5px;font-weight:700;border-right:1px solid rgba(255,255,255,.18)}
.header-rule{left:0;top:68px;width:290px;height:3px;background:var(--blue)}

/* hero */
.hero-photo{left:0;top:72px;width:772px;height:302px;background:linear-gradient(100deg,#7d8a6a 0%,#b7b2a6 30%,#d9d6cf 55%,#c9d3d6 75%,#8e9a8e 100%)}
.hero-caption{left:350px;top:278px;width:422px;height:66px;background:rgba(40,40,40,.85);clip-path:polygon(8px 0,100% 0,100% 100%,0 100%)}
.hero-caption .lead{position:absolute;left:31px;top:12px;font-size:15px;font-weight:700;color:var(--white)}
.hero-caption .claim{position:absolute;left:31px;top:35px;font-size:14px;color:var(--white);text-transform:none}

/* welcome */
.welcome-title{left:62px;top:404px;font-size:10.5px;color:#111}
.welcome-title span{color:var(--blue);text-transform:none}
.welcome-rule{left:62px;top:429px;width:386px;height:1px;background:#ddd}
.welcome-rule::before{content:"";position:absolute;left:0;top:-1px;width:60px;height:2px;background:var(--green)}
.welcome-lead{left:61px;top:441px;width:390px;font-size:8.6px;font-weight:900;line-height:1.45;color:#111}
.welcome-body{left:61px;top:474px;width:390px;font-size:7.4px;line-height:1.72;color:var(--grey-text)}
.btn-more{left:60px;top:532px;width:71px;height:23px;background:var(--green);color:var(--white);font-size:7.5px;font-weight:900;display:flex;align-items:center;justify-content:center}
.video{left:478px;top:408px;width:233px;height:147px;background:linear-gradient(135deg,#c8c4bc,#8d8780 55%,#3e3a36)}
.video-play{left:104px;top:57px;width:26px;height:26px;border-radius:50%;background:var(--white);display:flex;align-items:center;justify-content:center}
.video-bar{left:0;bottom:0;width:100%;height:15px;background:#111;color:var(--white);font-size:6px;font-weight:700;display:flex;align-items:center;padding:0 6px;gap:6px}
.video-track{flex:1;height:5px;border-radius:3px;background:#333;position:relative}
.video-track::before{content:"";position:absolute;left:18px;top:-1px;width:7px;height:7px;border-radius:50%;background:var(--blue)}

/* nature */
.nature{left:0;top:591px;width:772px;height:255px;background:radial-gradient(ellipse at 70% 30%,var(--teal) 0%,var(--teal-dark) 70%)}
.nature-title{left:0;top:26px;width:772px;text-align:center;font-size:11px;color:var(--white)}
.nature-rule{left:192px;top:51px;width:388px;height:1px;background:rgba(255,255,255,.25)}
.nature-rule::before{content:"";position:absolute;left:170px;top:-1px;width:54px;height:2px;background:var(--green-light)}
.machine{left:112px;top:76px;width:150px;height:150px;border-radius:50%;border:3px solid var(--blue);background:radial-gradient(circle at 50% 50%,#7fbf3d,#4f9a2d);box-shadow:0 0 0 3px rgba(255,255,255,.85)}
.feature{left:346px;display:flex;align-items:center;gap:14px;color:var(--white);font-size:8.8px;font-weight:700}
.feature-icon{width:29px;height:29px;border-radius:50%;background:var(--green);border:2px solid #dfe9e0;display:flex;align-items:center;justify-content:center}

/* lists */
.panel{top:883px;width:259px;height:223px;background:var(--panel);clip-path:polygon(0 0,100% 0,100% 100%,0 100%)}
.panel-head{height:30px;background:var(--blue);color:var(--white);font-size:11px;padding:10px 13px}
.panel ul{list-style:none;padding:12px 0 0 14px}
.panel li{height:19.3px;font-size:8.6px;color:#444;display:flex;align-items:center;gap:8px}
.panel-corner{position:absolute;right:0;bottom:0;width:18px;height:18px;background:var(--green-light);clip-path:polygon(100% 0,100% 100%,0 100%)}

/* footer */
.site-footer{left:0;top:1142px;width:772px;height:58px;background:var(--green)}
.social{left:60px;top:20px;display:flex;gap:3px}
.social span{width:21px;height:21px;background:rgba(255,255,255,.25)}
.footer-nav{right:61px;top:16px;font-size:8.3px;color:var(--white);word-spacing:1px}
.copyright{right:61px;top:35px;font-size:7.8px;color:var(--white);letter-spacing:.3px}
</style>
</head>
<body>

<header class="site-header abs">
  <div class="brand abs"><span class="brand-dot"></span><span class="brand-name">Velmora Steam Cleaning</span></div>
  <div class="address abs">
    <svg width="7" height="10" viewBox="0 0 7 10"><path d="M3.5 0A3.5 3.5 0 0 0 0 3.5C0 6 3.5 10 3.5 10S7 6 7 3.5A3.5 3.5 0 0 0 3.5 0zm0 5a1.4 1.4 0 1 1 0-2.8 1.4 1.4 0 0 1 0 2.8z" fill="#34a6d7"/></svg>
    48 Calle Marisol Ste. 12-204 Dorado, PR 00646
  </div>
  <nav class="main-nav abs">
    <ul>
      <li style="width:73px">HOME</li>
      <li style="width:85px">ABOUT US</li>
      <li style="width:105px">OUR SERVICES</li>
      <li style="width:78px">BENIFITS</li>
      <li style="width:95px;border:none">CONTACT US</li>
    </ul>
  </nav>
  <div class="header-rule abs"></div>
</header>

<section class="hero">
  <div class="hero-photo abs" role="img" aria-label="Bright glass-walled living room with armchairs and a smiling cleaner holding a basket of supplies"></div>
  <div class="hero-caption abs">
    <p class="lead">We are a</p>
    <p class="claim display">Commercial Cleaning Services</p>
  </div>
</section>

<section class="welcome">
  <h1 class="welcome-title abs display">Welcome to <span>Velmora Steam Cleaning</span></h1>
  <div class="welcome-rule abs"></div>
  <p class="welcome-lead abs">Lorem ipsum dolor sit amet, consectetur adipisicing elit, sed do eiusmod tem incididunt &nbsp;labore et dolore magna aliqua. Ut enim ad minim veniam.</p>
  <p class="welcome-body abs">Duis aute irure dolor in reprehenderitnin voliuptate velit esse cillum dolorie eu fugiat nulla &nbsp;Excepteur sint in occaecat cupidatat non proident, sunt in culpa qui officia deserunt mollit anim id est labo Neque i quisquam est, qui dolorem ipsum qus consectetur adipisci velit, sed quia non numii Uaam eius modi tempora incidunt ut labore et dol magnam aliquam quaerat voluptatem.</p>
  <div class="btn-more abs">READ MORE</div>
  <div class="video abs" role="img" aria-label="Demonstration video of a steam vacuum cleaning a wooden floor">
    <div class="video-play abs"><svg width="10" height="11" viewBox="0 0 10 11"><path d="M1 0l9 5.5L1 11z" fill="#111"/></svg></div>
    <div class="video-bar abs">
      <svg width="6" height="7" viewBox="0 0 6 7"><path d="M0 0l6 3.5L0 7z" fill="#fff"/></svg>
      <span>04:59</span>
      <div class="video-track"></div>
      <span>10:35</span>
      <svg width="9" height="8" viewBox="0 0 9 8"><path d="M0 2.5h2L5 0v8L2 5.5H0z" fill="#fff"/><path d="M6.5 2a3 3 0 0 1 0 4" stroke="#fff" fill="none"/></svg>
      <svg width="8" height="8" viewBox="0 0 8 8"><path d="M0 0h3L0 3zM8 8H5l3-3zM1 1l6 6" stroke="#fff" fill="#fff"/></svg>
    </div>
  </div>
</section>

<section class="nature abs">
  <h2 class="nature-title abs display">Nature of the Business &amp; Services</h2>
  <div class="nature-rule abs"></div>
  <svg class="abs" style="left:0;top:0" width="772" height="255">
    <g stroke="rgba(255,255,255,.3)" stroke-width=".8">
      <line x1="262" y1="151" x2="346" y2="96"/>
      <line x1="262" y1="151" x2="346" y2="133"/>
      <line x1="262" y1="151" x2="346" y2="170"/>
      <line x1="262" y1="151" x2="346" y2="206"/>
    </g>
  </svg>
  <div class="machine abs" role="img" aria-label="Blue portable steam cleaning machine"></div>
  <div class="feature abs" style="top:81px"><span class="feature-icon"><svg width="12" height="12" viewBox="0 0 12 12"><path d="M4 1h4M5 1v3L2 10h8L7 4V1" stroke="#fff" fill="none" stroke-width="1.3"/></svg></span>No chemicals or soaps involved</div>
  <div class="feature abs" style="top:118px"><span class="feature-icon"><svg width="12" height="12" viewBox="0 0 12 12"><path d="M3 11C3 5 6 2 10 1c0 5-2 8-6 9" fill="#fff"/></svg></span>Safe and eco-friendly green cleaning</div>
  <div class="feature abs" style="top:155px"><span class="feature-icon"><svg width="12" height="12" viewBox="0 0 12 12"><path d="M1.5 6.5l3 3 6-7" stroke="#fff" fill="none" stroke-width="2"/></svg></span>Cleans, sanitizes, deodorizes and disinfects all at the same time</div>
  <div class="feature abs" style="top:191px"><span class="feature-icon"><svg width="12" height="12" viewBox="0 0 12 12"><g stroke="#fff" stroke-width="1.4"><line x1="6" y1="0" x2="6" y2="12"/><line x1="0" y1="6" x2="12" y2="6"/><line x1="2" y1="2" x2="10" y2="10"/><line x1="10" y1="2" x2="2" y2="10"/></g></svg></span>Causes no allergies</div>
</section>

<section class="panel abs" style="left:115px">
  <h3 class="panel-head display">Opportunities</h3>
  <ul>
    <li><svg width="8" height="8" viewBox="0 0 8 8"><rect x=".5" y="1.5" width="6" height="6" fill="none" stroke="#999"/><path d="M2 4l1.5 1.5L7.5 1" stroke="#777" fill="none"/></svg>Auto Steam Cleaning</li>
    <li><svg width="8" height="8" viewBox="0 0 8 8"><rect x=".5" y="1.5" width="6" height="6" fill="none" stroke="#999"/><path d="M2 4l1.5 1.5L7.5 1" stroke="#777" fill="none"/></svg>Carpet Steam Cleaning</li>
    <li><svg width="8" height="8" viewBox="0 0 8 8"><rect x=".5" y="1.5" width="6" height="6" fill="none" stroke="#999"/><path d="M2 4l1.5 1.5L7.5 1" stroke="#777" fill="none"/></svg>Industrial Steam Cleaning</li>
    <li><svg width="8" height="8" viewBox="0 0 8 8"><rect x=".5" y="1.5" width="6" height="6" fill="none" stroke="#999"/><path d="M2 4l1.5 1.5L7.5 1" stroke="#777" fill="none"/></svg>Furniture</li>
    <li><svg width="8" height="8" viewBox="0 0 8 8"><rect x=".5" y="1.5" width="6" height="6" fill="none" stroke="#999"/><path d="M2 4l1.5 1.5L7.5 1" stroke="#777" fill="none"/></svg>Boats of all sizes</li>
    <li><svg width="8" height="8" viewBox="0 0 8 8"><rect x=".5" y="1.5" width="6" height="6" fill="none" stroke="#999"/><path d="M2 4l1.5 1.5L7.5 1" stroke="#777" fill="none"/></svg>Awnings, blinds and shutters</li>
    <li><svg width="8" height="8" viewBox="0 0 8 8"><rect x=".5" y="1.5" width="6" height="6" fill="none" stroke="#999"/><path d="M2 4l1.5 1.5L7.5 1" stroke="#777" fill="none"/></svg>Cleaning after renovation of buildings</li>
    <li><svg width="8" height="8" viewBox="0 0 8 8"><rect x=".5" y="1.5" width="6" height="6" fill="none" stroke="#999"/><path d="M2 4l1.5 1.5L7.5 1" stroke="#777" fill="none"/></svg>Remove bacteria, yeast, molds &amp; fungi</li>
    <li><svg width="8" height="8" viewBox="0 0 8 8"><rect x=".5" y="1.5" width="6" height="6" fill="none" stroke="#999"/><path d="M2 4l1.5 1.5L7.5 1" stroke="#777" fill="none"/></svg>Sanitize equipment used for food &amp; beverage</li>
  </ul>
  <span class="panel-corner"></span>
</section>

<section class="panel abs" style="left:398px">
  <h3 class="panel-head display">Benefits</h3>
  <ul>
    <li><svg width="8" height="8" viewBox="0 0 8 8"><rect x=".5" y="1.5" width="6" height="6" fill="none" stroke="#999"/><path d="M2 4l1.5 1.5L7.5 1" stroke="#777" fill="none"/></svg>Quickly, easily removes dirt, stains &amp; grease</li>
    <li><svg width="8" height="8" viewBox="0 0 8 8"><rect x=".5" y="1.5" width="6" height="6" fill="none" stroke="#999"/><path d="M2 4l1.5 1.5L7.5 1" stroke="#777" fill="none"/></svg>Reduce water &amp; chemical consumption</li>
    <li><svg width="8" height="8" viewBox="0 0 8 8"><rect x=".5" y="1.5" width="6" height="6" fill="none" stroke="#999"/><path d="M2 4l1.5 1.5L7.5 1" stroke="#777" fill="none"/></svg>Clean hard to reach nooks &amp; crannies</li>
    <li><svg width="8" height="8" viewBox="0 0 8 8"><rect x=".5" y="1.5" width="6" height="6" fill="none" stroke="#999"/><path d="M2 4l1.5 1.5L7.5 1" stroke="#777" fill="none"/></svg>Eliminate waste-water &amp; overspray</li>
    <li><svg width="8" height="8" viewBox="0 0 8 8"><rect x=".5" y="1.5" width="6" height="6" fill="none" stroke="#999"/><path d="M2 4l1.5 1.5L7.5 1" stroke="#777" fill="none"/></svg>Two operators can clean at once</li>
    <li><svg width="8" height="8" viewBox="0 0 8 8"><rect x=".5" y="1.5" width="6" height="6" fill="none" stroke="#999"/><path d="M2 4l1.5 1.5L7.5 1" stroke="#777" fill="none"/></svg>Deodorize &amp; sterilize surfaces</li>
    <li><svg width="8" height="8" viewBox="0 0 8 8"><rect x=".5" y="1.5" width="6" height="6" fill="none" stroke="#999"/><path d="M2 4l1.5 1.5L7.5 1" stroke="#777" fill="none"/></svg>Easy to maintain &amp; operate</li>
    <li><svg width="8" height="8" viewBox="0 0 8 8"><rect x=".5" y="1.5" width="6" height="6" fill="none" stroke="#999"/><path d="M2 4l1.5 1.5L7.5 1" stroke="#777" fill="none"/></svg>Continuous, on-demand steam</li>
    <li><svg width="8" height="8" viewBox="0 0 8 8"><rect x=".5" y="1.5" width="6" height="6" fill="none" stroke="#999"/><path d="M2 4l1.5 1.5L7.5 1" stroke="#777" fill="none"/></svg>Quiet &amp; low exhaust outputve t</li>
  </ul>
  <span class="panel-corner"></span>
</section>

<footer class="site-footer abs">
  <div class="social abs"><span></span><span></span><span></span></div>
  <p class="footer-nav abs">HOME &nbsp;&nbsp;| &nbsp;&nbsp;ABOUT US &nbsp;&nbsp;| &nbsp;&nbsp;OUR SERVICES &nbsp;&nbsp;| &nbsp;&nbsp;BENIFITS &nbsp;&nbsp;| &nbsp;&nbsp;CONTACT US</p>
  <p class="copyright abs">Copyright 2015 Velmora Steam Cleaning. All Rights Reserved.</p>
</footer>

</body>
</html>
```